Templates for Construction Company

We are looking to have templates prepared for all aspects of our letter sending. Using our brand design. with similar layouts that look the same.

Letterheads design & Email signatures

We use letter heads for - quotes, contract correspondence, variations, formal letters, invitations

Target Market(s)

Clients documents sent in emails

Industry/Entity Type

Construction

Font styles to use
Serif
Sans Serif

Colors
0054AA
0677BA
7BADD7
CADEEF
E8F1F8

Requirements
Must have
• Easy to read, water marks on page
Nice to have
• Different options for different letters

```html
<!DOCTYPE html>
<html lang="en">
<head>
<meta charset="utf-8">
<title>Framewell Building Group – Letterhead &amp; Email Signature</title>
<link rel="stylesheet" href="https://fonts.googleapis.com/css2?family=Open+Sans:wght@400;600&family=Lato:wght@400;700&display=swap">
<style>
  :root {
    --brand-blue: #5b8ac9;
    --ink: #3d3d3d;
    --ink-soft: #555555;
    --rule-grey: #6a6a6a;
    --paper: #ffffff;
    --backdrop: #e9eaec;
    --signature-tone: #d9dde3;
  }
  * { box-sizing: border-box; margin: 0; padding: 0; }
  html, body { width: 912px; height: 1200px; overflow: hidden; }
  body {
    background: var(--backdrop);
    position: relative;
    font-family: "Open Sans", Arial, sans-serif;
    color: var(--ink);
  }

  /* ---------- Letterhead ---------- */
  .letterhead {
    position: absolute;
    left: 106px; top: 28px;
    width: 700px; height: 900px;
    background: var(--paper);
    box-shadow: 0 2px 8px rgba(0,0,0,.12);
  }
  .brand {
    position: absolute;
    display: flex; align-items: center; gap: 10px;
    color: var(--brand-blue);
    font-family: "Open Sans", Arial, sans-serif;
    font-weight: 600;
    white-space: nowrap;
  }
  .letterhead .brand { left: 252px; top: 48px; font-size: 34px; }
  .brand-square { width: 22px; height: 22px; background: var(--brand-blue); flex: none; }

  .letter-body {
    position: absolute;
    left: 66px; top: 160px; width: 564px;
    font-size: 11px; line-height: 20px; color: var(--ink-soft);
  }
  .issue-date { margin-bottom: 12px; }
  .recipient { line-height: 13.5px; margin-bottom: 36px; }
  .salutation { margin-bottom: 20px; }
  .letter-body p.paragraph { margin-bottom: 20px; text-align: justify; }
  .closing { margin-top: 30px; }
  .signature-mark {
    width: 160px; height: 22px; margin: 10px 0 6px;
    background: linear-gradient(90deg, var(--signature-tone), #eef0f3);
    border-radius: 3px;
  }
  .signatory-name { font-size: 13.5px; color: var(--ink); line-height: 20px; }
  .signatory-role { font-size: 11px; line-height: 18px; }

  .letter-address {
    position: absolute; left: 0; right: 0; top: 836px;
    text-align: center; font-family: Arial, sans-serif;
    font-size: 13px; color: #111;
  }
  .letter-contact-band {
    position: absolute; left: 0; right: 0; bottom: 0; height: 36px;
    background: var(--brand-blue);
    color: #fff; font-family: "Lato", Arial, sans-serif; font-size: 13px;
    display: flex; align-items: center; justify-content: center; gap: 6px;
  }
  .letter-contact-band b { font-weight: 700; }

  /* ---------- Email signature ---------- */
  .email-signature {
    position: absolute;
    left: 106px; top: 958px;
    width: 700px; height: 210px;
    background: var(--paper);
    box-shadow: 0 2px 8px rgba(0,0,0,.12);
    font-family: "Lato", Arial, sans-serif;
  }
  .email-signature .brand { left: 40px; top: 72px; font-size: 26px; gap: 8px; }
  .email-signature .brand-square { width: 18px; height: 18px; }
  .signature-divider {
    position: absolute; left: 224px; top: 34px;
    width: 1.5px; height: 128px; background: var(--rule-grey);
  }
  .signature-details { position: absolute; left: 248px; top: 28px; }
  .signature-name { font-size: 23px; color: var(--brand-blue); line-height: 26px; }
  .signature-role { font-size: 17px; color: var(--ink); line-height: 20px; margin-bottom: 6px; }
  .contact-line {
    display: flex; align-items: center; gap: 8px;
    font-size: 16.5px; color: var(--ink); line-height: 20.5px;
  }
  .contact-line svg { width: 16px; height: 16px; flex: none; fill: var(--brand-blue); }
  .signature-address-band {
    position: absolute; left: 0; right: 0; bottom: 0; height: 34px;
    background: var(--brand-blue); color: #fff;
    font-size: 16.5px; display: flex; align-items: center;
    padding-left: 248px;
  }
</style>
</head>
<body>

<section class="letterhead" aria-label="Company letterhead">
  <div class="brand"><span class="brand-square"></span>Framewell</div>

  <div class="letter-body">
    <p class="issue-date">Issuing Date: May 5, 2018</p>
    <p class="recipient">Name Of Employee Mr. Dalton<br>Address of Employee<br>Address Line 2 etc..</p>
    <p class="salutation">Dear Mr. Dalton</p>
    <p class="paragraph">Lorem Ipsum has been the industry's standard dummy text ever since the 1500s, when an unknown printer took a galley of type and scrambled it to make a type specimen book. It has survived not only five centuries, but also the leap into electronic typesetting, remaining essentially unchanged. It was popularised in the 1960s with the release of Setwell sheets containing Lorem Ipsum passages, and more recently with desktop publishing software like Pagecraft Studio including versions of Lorem Ipsum.</p>
    <p class="paragraph">Lorem Ipsum is simply dummy text of the printing and typesetting industry. Lorem Ipsum has been the industry's standard dummy text ever since the 1500s, when an unknown printer took a galley of type and scrambled it to make a type specimen book.</p>
    <p class="paragraph">It has survived not only five centuries, but also the leap into electronic typesetting, remaining essentially unchanged. It was popularised in the 1960s with the release of Setwell sheets containing Lorem Ipsum passages.</p>
    <p class="closing">Yours Sincerely</p>
    <div class="signature-mark" role="img" aria-label="Handwritten signature"></div>
    <p class="signatory-name">Marcus Hale</p>
    <p class="signatory-role">Managing Director</p>
  </div>

  <p class="letter-address">88 Harbour Row, Suite 4, 30917, Eastvale</p>
  <div class="letter-contact-band">
    <span><b>P:</b> 055-210 348 671</span>
    <span>| <b>E:</b> hello@framewellgroup.com</span>
    <span>| <b>www.framewellgroup.com</b></span>
  </div>
</section>

<section class="email-signature" aria-label="Email signature">
  <div class="brand"><span class="brand-square"></span>Framewell</div>
  <div class="signature-divider"></div>
  <div class="signature-details">
    <p class="signature-name">Marcus Hale</p>
    <p class="signature-role">Managing Director</p>
    <p class="contact-line">
      <svg viewBox="0 0 16 16" aria-hidden="true"><path d="M4 0h8a1.5 1.5 0 0 1 1.5 1.5v13A1.5 1.5 0 0 1 12 16H4a1.5 1.5 0 0 1-1.5-1.5v-13A1.5 1.5 0 0 1 4 0zm0 2v10h8V2zm4 11a1 1 0 1 0 0 2 1 1 0 0 0 0-2z"/></svg>
      055-210 348 671</p>
    <p class="contact-line">
      <svg viewBox="0 0 16 16" aria-hidden="true"><path d="M1 5c0-2 3-3 7-3s7 1 7 3v1.5h-3.5V5h-7v1.5H1zM3.5 7h9l2 7h-13zM8 8.5a2.2 2.2 0 1 0 0 4.4 2.2 2.2 0 0 0 0-4.4z"/></svg>
      055-210 348 671</p>
    <p class="contact-line">
      <svg viewBox="0 0 16 16" aria-hidden="true"><path d="M0 3h16v10H0zm1.5 1.2v.3L8 9l6.5-4.5v-.3zm0 2.1v5.5h13V6.3L8 10.8z"/></svg>
      hello@framewellgroup.com</p>
    <p class="contact-line">
      <svg viewBox="0 0 16 16" aria-hidden="true"><path d="M8 0a8 8 0 1 1 0 16A8 8 0 0 1 8 0zm-2 3C4 4 3 6 3.5 8l3 1 .5 3 2 1-1-3 2-2-2-1-1-2 1-2z"/></svg>
      www.framewellgroup.com</p>
  </div>
  <div class="signature-address-band">88 Harbour Row, Suite 4, 30917, Eastvale</div>
</section>

</body>
</html>
```